Varden Ridge Concrete Pumping needs a logo design and is in the concrete industry

A creative design for this Varden Ridge Concrete Pumping business. Using a trailer mounted line pump, not a boom pump.
Colour to be used is orange and a mix of white or black writing.
Target Market(s)
General Public, anyone
Industry/Entity Type
Concrete
Contact Information for Business Card
Varden Ridge Concrete Pumping
Brennan Holloway
PO BOX 47
Varden VIC 3288
Phone: 0491552083
Email: Holloway@postwren.com.au
Colors
f37122
000000
ffffff
Requirements
Must have
- Details listed
Nice to have
- A great logo
Should not have
- anything silly

```html
<!DOCTYPE html>
<html lang="en">
<head>
<meta charset="utf-8">
<title>Varden Ridge Concrete Pumping – Business Cards</title>
<link rel="stylesheet" href="https://fonts.googleapis.com/css2?family=Questrial&display=swap">
<style>
  :root {
    --orange: #f37122;
    --black: #000000;
    --white: #ffffff;
    --backdrop: #d9d9d6;
    --ink: #1a1a1a;
  }
  * { box-sizing: border-box; margin: 0; padding: 0; }
  html, body { width: 1200px; height: 873px; overflow: hidden; }
  body {
    background: var(--backdrop);
    font-family: "Questrial", "Century Gothic", sans-serif;
    display: flex;
    align-items: center;
    justify-content: center;
    gap: 60px;
  }
  .card {
    position: relative;
    width: 525px;
    height: 300px;
    background: var(--white);
    box-shadow: 0 6px 18px rgba(0,0,0,0.18);
    overflow: hidden;
  }

  /* Front */
  .card-front .band {
    position: absolute;
    left: 0; right: 0;
    height: 40px;
    background: var(--black);
  }
  .card-front .band-top { top: 0; }
  .card-front .band-bottom { bottom: 0; }
  .brand {
    display: flex;
    align-items: center;
    gap: 10px;
    color: var(--orange);
    white-space: nowrap;
  }
  .brand-dot {
    width: 14px; height: 14px;
    border-radius: 50%;
    background: var(--orange);
    flex: none;
  }
  .card-front .brand {
    position: absolute;
    top: 50%; left: 50%;
    transform: translate(-50%, -50%);
    font-size: 27px;
  }
  .card-front .brand-dot { width: 20px; height: 20px; }

  /* Back */
  .card-back .stripe {
    position: absolute;
    left: 0; right: 0;
    height: 10px;
    background: var(--orange);
  }
  .card-back .stripe-top { top: 16px; }
  .card-back .stripe-bottom { bottom: 16px; }
  .card-back .brand {
    position: absolute;
    top: 50px; left: 36px;
    font-size: 14px;
  }
  .card-back .brand-dot { width: 10px; height: 10px; }
  .name-panel {
    position: absolute;
    right: 0;
    top: 92px;
    width: 250px;
    height: 112px;
    background: var(--orange);
    border-radius: 56px 0 0 56px;
    color: var(--white);
    text-align: right;
    padding: 20px 22px 0 0;
  }
  .person-name { font-size: 27px; line-height: 1.1; }
  .address { font-size: 14px; line-height: 1.25; margin-top: 6px; }
  .contact-list {
    position: absolute;
    left: 36px;
    top: 150px;
    list-style: none;
    color: var(--ink);
    font-size: 17px;
  }
  .contact-list li {
    display: flex;
    align-items: center;
    gap: 12px;
    margin-bottom: 8px;
  }
  .contact-icon { width: 20px; height: 20px; flex: none; }
</style>
</head>
<body>

  <section class="card card-front" aria-label="Business card front">
    <div class="band band-top"></div>
    <div class="brand">
      <span class="brand-dot"></span>
      <span class="brand-name">Varden Ridge Concrete Pumping</span>
    </div>
    <div class="band band-bottom"></div>
  </section>

  <section class="card card-back" aria-label="Business card back">
    <div class="stripe stripe-top"></div>
    <div class="brand">
      <span class="brand-dot"></span>
      <span class="brand-name">Varden Ridge Concrete Pumping</span>
    </div>

    <div class="name-panel">
      <p class="person-name">Brennan Holloway</p>
      <p class="address">PO BOX 47<br>Varden VIC 3288</p>
    </div>

    <ul class="contact-list">
      <li>
        <svg class="contact-icon" viewBox="0 0 20 20" aria-hidden="true">
          <circle cx="10" cy="10" r="9.5" fill="var(--orange)"/>
          <rect x="7" y="4.5" width="6" height="11" rx="1" fill="none" stroke="#fff" stroke-width="1.3"/>
          <circle cx="10" cy="13.3" r="0.7" fill="#fff"/>
        </svg>
        <span>0491552083</span>
      </li>
      <li>
        <svg class="contact-icon" viewBox="0 0 20 20" aria-hidden="true">
          <circle cx="10" cy="10" r="9.5" fill="var(--orange)"/>
          <rect x="5" y="6.5" width="10" height="7" fill="none" stroke="#fff" stroke-width="1.3"/>
          <path d="M5 6.5 L10 10.5 L15 6.5" fill="none" stroke="#fff" stroke-width="1.3"/>
        </svg>
        <span>Holloway@postwren.com.au</span>
      </li>
    </ul>
    <div class="stripe stripe-bottom"></div>
  </section>

</body>
</html>
```